Poster Design Project

About Us
Brimco is a company that specializes in providing communication solutions to the travel market. Our simple vision of “every hotel should have a mobile phone in the guest rooms”, led us to develop a path breaking cost effective mobile phone. With full integration capabilities with the hotels property management system, location based marketing, user locator and other features, this product is unique in addressing the hospitality segment.
Product Placement
The Brimco mobile will be placed in the hotel room on an A4 Sized transparent stand (the transparent stand is attached for your reference. If you notice, the phone will be placed in the jacket on the bottom left and in another jacket on the bottom right will be the brochure. So effectively, the design space available on the A4 brochure is only 60% of the space). The designed poster that we wish designed will be inserted in the A4 sized acrylic stand. The stand would typically be on the bedside table or on the study table of the hotel room. The A4 design should be bright and vibrant in keeping with our logo colors.
Attached is our logo. Also attached is the symbol of our phone that could be used innovatively on the brochure if you think it helps.
Attached is the content for the poster.
Reason: Feedback from the management team got delayed, hence the extension. Thanks
Reason: The delay is in the content finalization.

```html
<!DOCTYPE html>
<html lang="en">
<head>
<meta charset="utf-8">
<title>Brimco – Keep Talking Poster</title>
<link href="https://fonts.googleapis.com/css2?family=Source+Sans+3:wght@400;600;700&display=swap" rel="stylesheet">
<style>
  :root{
    --ink:#111111;
    --white:#ffffff;
    --red:#f5260a;
    --yellow:#ffe21a;
    --panel-brown:rgba(120,70,30,0.82);
  }
  *{margin:0;padding:0;box-sizing:border-box}
  html,body{width:848px;height:1200px;overflow:hidden;background:var(--white)}
  .poster{position:relative;width:848px;height:1200px;overflow:hidden;background:var(--white);font-family:"Source Sans 3",sans-serif;color:var(--ink)}
  .wave-bg{position:absolute;left:0;top:0;width:848px;height:1200px}

  .brand{position:absolute;left:0;top:40px;width:848px;text-align:center}
  .brand-name{font-weight:700;font-size:76px;line-height:1;color:var(--ink)}

  .headline{position:absolute;left:0;top:166px;width:848px;font-size:49px;line-height:52px;font-weight:400}
  .headline .line-one{position:absolute;left:174px;top:0;white-space:nowrap}
  .headline .line-two{position:absolute;left:349px;top:52px;white-space:nowrap}

  .offer-circle{position:absolute;left:31px;top:306px;width:400px;height:400px;border-radius:50%;background:var(--red);border:6px solid var(--white);box-shadow:0 2px 8px rgba(0,0,0,0.15)}
  .offer-list{position:absolute;left:0;top:92px;width:388px;text-align:center;transform:rotate(-15deg);color:var(--white);font-size:21px;line-height:26px}
  .offer-list .hl{color:var(--yellow);font-size:27px;font-weight:600}
  .offer-list .plus{display:block;line-height:20px}
  .offer-list .price{color:var(--yellow);font-size:27px;font-weight:600}

  .info-panel{position:absolute;left:483px;top:397px;width:336px;height:243px;border-radius:10px;background:var(--panel-brown);padding:12px 10px 0 11px;color:var(--white);font-size:22px;line-height:25.5px}
  .info-title{color:var(--yellow);font-size:30px;font-weight:400;text-align:center;margin-bottom:18px}
  .info-body{white-space:nowrap}
  .info-body .hl{color:var(--yellow)}
  .info-more{color:var(--yellow);font-size:23px;text-align:center;margin-top:26px}

  .phone-jacket{position:absolute;left:492px;top:685px;width:320px;height:484px;border-radius:12px;background:rgba(255,255,255,0.55)}
  .phone-render{position:absolute;left:28px;top:25px;width:264px;height:440px;border-radius:44px;background:linear-gradient(160deg,#6b6b6b 0%,#1b1b1b 35%,#2a2a2a 70%,#0c0c0c 100%);border:6px solid #c9c9c9}
  .jacket-base{position:absolute;left:56px;top:467px;width:208px;height:4px;background:var(--white)}
</style>
</head>
<body>
<main class="poster">
  <svg class="wave-bg" viewBox="0 0 848 1200" preserveAspectRatio="none" aria-hidden="true">
    <defs>
      <linearGradient id="waveFill" x1="0" y1="0" x2="0" y2="1">
        <stop offset="0" stop-color="#ffa640"/>
        <stop offset="0.35" stop-color="#ff7a24"/>
        <stop offset="1" stop-color="#ff4a08"/>
      </linearGradient>
    </defs>
    <path d="M0 262 C180 250 330 290 520 305 C680 318 780 330 848 345 L848 1200 L0 1200 Z" fill="url(#waveFill)"/>
    <path d="M0 320 C250 290 520 330 848 420 L848 520 C600 420 300 360 0 380 Z" fill="#ffb060" opacity="0.45"/>
    <path d="M0 640 C250 560 520 620 848 700 L848 760 C560 680 280 640 0 700 Z" fill="#ffc37a" opacity="0.35"/>
    <path d="M0 880 C260 800 560 830 848 900 L848 980 C560 900 260 880 0 960 Z" fill="#ff8a3a" opacity="0.35"/>
  </svg>

  <header class="brand">
    <span class="brand-name">Brimco</span>
  </header>

  <h1 class="headline">
    <span class="line-one">Pick up this phone NOW,</span>
    <span class="line-two">to keep talking...</span>
  </h1>

  <section class="offer-circle">
    <p class="offer-list">
      <span class="hl">SAVE 80%</span> on international<br>roaming
      <span class="plus">+</span>
      Get a <span class="hl">LOCAL</span> number
      <span class="plus">+</span>
      <span class="hl">60 FREE</span> minutes of<br>international Calls
      <span class="plus">+</span>
      <span class="hl">60 FREE</span> minutes of local calls
      <span class="plus">+</span>
      <span class="price">= 499 BHT</span>
    </p>
  </section>

  <aside class="info-panel">
    <h2 class="info-title">Brimco. Keep Talking.</h2>
    <p class="info-body"><span class="hl">The following needs to appear as<br>blurbs</span> - Itemized bill on checkout<br>Flexible tariff plans to choose from<br>Excellent call quality</p>
    <p class="info-more">Refer to the brochure for more:</p>
  </aside>

  <div class="phone-jacket">
    <div class="phone-render" role="img" aria-label="Product render of the in-room smartphone with keyboard, standing in the acrylic jacket"></div>
    <div class="jacket-base"></div>
  </div>
</main>
</body>
</html>
```